Roadside building business signage for a holistic health clinic.

Replace signs as shown in the attached file. They are perforated stickers that go on the windows as shown. Looking for something that has our logo and says the name of the practice with logo (Fernbrook Health & Wellness) also boldly says Acupuncture, IV Vitamins, and Holistic Health.
Possibly our phone number as well 538-207-6145

Please don't use pink except the logo. Earthy, organic tone colors appreciated.

Need of eye catching window signage of a holistic clinic on a brick building. Pink, purple, sage green, white color. Logo is pink on a white background. Please don't overload with too much pink. Words to include are "Fernbrook Health and Wellness(name of business)", "Direct Primary Care", " Medical acupuncture", "IV Vitamin Therapy", "fernbrookwholecare-example.com","538-207-6145".

Target Market(s)

People will see in their cars passing by the building. Busy roadside so need to be visible while passing in fast speed.

Industry/Entity Type

Health & Wellness

Font styles to use
Sans Serif

Colors

Designer to choose colors to be used in the design.

Requirements
Must have
• On sign must have words Holistic Medicine, Medical Acupuncture, Direct Primary Care and IV vitamins.
Nice to have
• Simple, minimalistic, artistic yet has clear message. White, Black, Violet, Pink (logo), Dark green, Sage green.
Should not have
• Bold colors (red, yellow, blue), same tone colors. Blue waves on the current signage (uploaded file) must go.

```html
<!DOCTYPE html>
<html lang="en">
<head>
<meta charset="utf-8">
<title>Fernbrook Health &amp; Wellness — Window Signage</title>
<link rel="stylesheet" href="https://fonts.googleapis.com/css2?family=Raleway:wght@500;700;800&family=Oswald:wght@500;600&display=swap">
<style>
  :root{
    --backdrop:#a3a3a3;
    --cream:#ecebe4;
    --sage-dark:#3e4e45;
    --sage:#8fa58f;
    --sage-light:#b7c6b4;
    --ink:#33443b;
    --pink:#e2187a;
    --white:#ffffff;
    --panel:149px;
  }
  *{box-sizing:border-box;margin:0;padding:0}
  html,body{width:1200px;height:515px;overflow:hidden}
  body{background:var(--backdrop);position:relative;font-family:"Raleway",sans-serif}

  .panel{position:absolute;width:var(--panel);height:var(--panel);overflow:hidden;
    display:flex;flex-direction:column;align-items:center;justify-content:center;text-align:center}
  .panel--cream{background:var(--cream);color:var(--ink)}
  .panel--green{background:var(--sage-dark);color:var(--white)}

  .row-arch{top:24px}
  .row-top{top:181px}
  .row-bottom{top:338px}
  .col-1{left:211px}.col-2{left:368px}.col-3{left:525px}.col-4{left:682px}.col-5{left:839px}

  .arch-left{border-top-left-radius:100% 100%}
  .arch-right{border-top-right-radius:100% 100%}

  /* decoration placeholders */
  .wave{position:absolute;top:0;right:0;width:70px;height:36px}
  .wave--left{left:0;right:auto}
  .panel--cream .wave{background:linear-gradient(200deg,rgba(255,255,255,.95),rgba(255,255,255,0) 75%)}
  .panel--cream .wave--left{background:linear-gradient(160deg,rgba(255,255,255,.95),rgba(255,255,255,0) 75%)}
  .panel--green .wave{background:linear-gradient(200deg,rgba(183,198,180,.75),rgba(183,198,180,0) 75%)}
  .panel--green .wave--left{background:linear-gradient(160deg,rgba(183,198,180,.75),rgba(183,198,180,0) 75%)}
  .leaf{position:absolute;bottom:0;width:44px;height:26px;border-radius:44px 44px 0 0}
  .leaf--left{left:0;background:linear-gradient(20deg,rgba(143,165,143,.55),rgba(143,165,143,0) 80%)}
  .leaf--right{right:0;background:linear-gradient(-20deg,rgba(143,165,143,.55),rgba(143,165,143,0) 80%)}

  .arch-content{margin-top:42px;display:flex;flex-direction:column;align-items:center}
  .brand-dot{width:22px;height:22px;border-radius:50%;background:var(--pink);margin-bottom:8px}
  .brand-name{font-weight:500;color:var(--sage-dark);line-height:1.05}
  .brand-name .line-main{display:block;font-size:18px;letter-spacing:2px;text-transform:uppercase}
  .brand-name .line-sub{display:block;font-size:6.5px;letter-spacing:2.2px;text-transform:uppercase;margin-top:3px}

  .call-label{font-weight:700;color:var(--sage);font-size:15px;margin-bottom:1px}
  .phone{font-family:"Oswald",sans-serif;font-weight:500;font-size:24px;color:var(--ink);line-height:1.1;letter-spacing:-.3px}
  .web-pill{margin-top:5px;background:var(--sage-dark);color:var(--white);font-family:"Oswald",sans-serif;
    font-weight:500;font-size:8.6px;padding:2px 5px;border-radius:5px;white-space:nowrap}

  .practice-name{font-weight:700;font-size:22px;line-height:1.05}

  .service-dot{width:11px;height:11px;border-radius:50%;background:var(--pink);margin-bottom:7px}
  .service{font-weight:700;text-transform:uppercase;line-height:.98}
  .service--holistic{font-size:25px}
  .service--iv{font-size:21px}
  .service--dpc{font-size:20px}
  .service--medical .main{display:block;font-size:27px;font-weight:800}
  .service--medical .sub{display:block;font-size:13.5px;font-weight:700;margin-top:2px}
</style>
</head>
<body>
  <main class="signage-set" aria-label="Window signage panels">

    <section class="panel panel--cream arch-left row-arch col-3">
      <div class="wave" role="img" aria-label="White flowing wave decoration"></div>
      <div class="arch-content">
        <span class="brand-dot"></span>
        <p class="brand-name"><span class="line-main">Fernbrook</span><span class="line-sub">Health &amp; Wellness</span></p>
      </div>
      <div class="leaf leaf--left" role="img" aria-label="Line-art leaf decoration"></div>
    </section>
    <section class="panel panel--cream arch-right row-arch col-4">
      <div class="wave wave--left" role="img" aria-label="White flowing wave decoration"></div>
      <div class="arch-content">
        <span class="brand-dot"></span>
        <p class="brand-name"><span class="line-main">Fernbrook</span><span class="line-sub">Health &amp; Wellness</span></p>
      </div>
      <div class="leaf leaf--right" role="img" aria-label="Line-art leaf decoration"></div>
    </section>

    <section class="panel panel--cream row-top col-2">
      <div class="wave" role="img" aria-label="White flowing wave decoration"></div>
      <p class="call-label">Call Today</p>
      <p class="phone">538-207-6145</p>
      <p class="web-pill">fernbrookwholecare-example.com</p>
      <div class="leaf leaf--left" role="img" aria-label="Line-art leaf decoration"></div>
    </section>
    <section class="panel panel--green row-top col-3">
      <div class="wave wave--left" role="img" aria-label="Sage flowing wave decoration"></div>
      <p class="practice-name">Fernbrook<br>Health and<br>Wellness</p>
      <div class="leaf leaf--right" role="img" aria-label="Line-art leaf decoration"></div>
    </section>
    <section class="panel panel--green row-top col-4">
      <div class="wave wave--left" role="img" aria-label="Sage flowing wave decoration"></div>
      <p class="practice-name">Fernbrook<br>Health and<br>Wellness</p>
      <div class="leaf leaf--right" role="img" aria-label="Line-art leaf decoration"></div>
    </section>
    <section class="panel panel--cream row-top col-5">
      <div class="wave" role="img" aria-label="White flowing wave decoration"></div>
      <p class="call-label">Call Today</p>
      <p class="phone">538-207-6145</p>
      <p class="web-pill">fernbrookwholecare-example.com</p>
      <div class="leaf leaf--left" role="img" aria-label="Line-art leaf decoration"></div>
    </section>

    <section class="panel panel--cream row-bottom col-1">
      <div class="wave" role="img" aria-label="White flowing wave decoration"></div>
      <span class="service-dot"></span>
      <p class="service service--holistic">Holistic<br>Health</p>
      <div class="leaf leaf--left" role="img" aria-label="Line-art leaf decoration"></div>
    </section>
    <section class="panel panel--green row-bottom col-2">
      <div class="wave" role="img" aria-label="Sage flowing wave decoration"></div>
      <span class="service-dot"></span>
      <p class="service service--medical"><span class="main">Medical</span><span class="sub">Acupuncture</span></p>
      <div class="leaf leaf--left" role="img" aria-label="Line-art leaf decoration"></div>
    </section>
    <section class="panel panel--cream row-bottom col-3">
      <div class="wave wave--left" role="img" aria-label="White flowing wave decoration"></div>
      <span class="service-dot"></span>
      <p class="service service--iv">IV Vitamin<br>Therapy</p>
      <div class="leaf leaf--right" role="img" aria-label="Line-art leaf decoration"></div>
    </section>
    <section class="panel panel--cream row-bottom col-4">
      <div class="wave" role="img" aria-label="White flowing wave decoration"></div>
      <span class="service-dot"></span>
      <p class="service service--dpc">Direct<br>Primary<br>Care</p>
      <div class="leaf leaf--left" role="img" aria-label="Line-art leaf decoration"></div>
    </section>
    <section class="panel panel--green row-bottom col-5">
      <div class="wave" role="img" aria-label="Sage flowing wave decoration"></div>
      <span class="service-dot"></span>
      <p class="service service--medical"><span class="main">Medical</span><span class="sub">Acupuncture</span></p>
      <div class="leaf leaf--left" role="img" aria-label="Line-art leaf decoration"></div>
    </section>

  </main>
</body>
</html>
```